Business Card Design Project

We need a business card design for a new company focused on educational technology called 'Bright Harbor Educational Consulting'. We are a consulting company that helps other technology companies and schools market their solutions.

The final design should communicate the positive future of education, which is digital.

Industry/Entity Type

Business

Requirements
Nice to have
• four color, front and back.

```html
<!DOCTYPE html>
<html lang="en">
<head>
<meta charset="utf-8">
<title>Bright Harbor Educational Consulting – Business Cards</title>
<link href="https://fonts.googleapis.com/css2?family=Open+Sans:wght@400;600;700&display=swap" rel="stylesheet">
<style>
  :root {
    --page-bg: #e6e6e6;
    --blue-light: #4a9ae0;
    --blue-mid: #2a6fc4;
    --blue-deep: #1b4e9c;
    --orange: #f29a1f;
    --ink: #2b2b2b;
    --ink-soft: #444;
    --white: #ffffff;
  }
  * { box-sizing: border-box; margin: 0; padding: 0; }
  html, body { width: 1200px; height: 944px; overflow: hidden; }
  body {
    background: var(--page-bg);
    font-family: "Open Sans", Arial, sans-serif;
    position: relative;
  }
  .card {
    position: absolute;
    width: 580px;
    height: 340px;
    border-radius: 26px;
    overflow: hidden;
    box-shadow: 0 8px 24px rgba(0,0,0,0.25);
  }
  /* Front */
  .card-front {
    left: 70px; top: 90px;
    background: radial-gradient(ellipse at 45% 40%, var(--blue-light) 0%, var(--blue-mid) 55%, var(--blue-deep) 100%);
    color: var(--white);
  }
  .front-lockup {
    position: absolute; left: 90px; top: 110px;
    display: flex; align-items: center; gap: 22px;
  }
  .front-mark {
    width: 58px; height: 58px; background: var(--white); opacity: 0.9;
  }
  .front-name {
    font-size: 30px; font-weight: 600; line-height: 1.15; letter-spacing: 0.5px;
    color: var(--white);
  }
  .front-web {
    position: absolute; left: 300px; top: 236px;
    font-size: 17px; font-weight: 600; letter-spacing: 1px;
  }
  /* Back */
  .card-back {
    left: 560px; top: 510px;
    background: var(--white);
    color: var(--ink);
  }
  .back-lockup {
    position: absolute; left: 44px; top: 50px;
    display: flex; align-items: center; gap: 14px;
  }
  .back-mark { width: 34px; height: 34px; background: var(--blue-mid); }
  .back-name {
    font-size: 17px; font-weight: 600; line-height: 1.2; color: var(--blue-deep);
  }
  .person {
    position: absolute; left: 390px; top: 100px;
  }
  .person-name { font-size: 22px; font-weight: 600; color: var(--ink); }
  .person-role { font-size: 15px; font-weight: 600; color: var(--orange); }
  .address {
    position: absolute; left: 44px; top: 170px;
    display: flex; gap: 10px;
    font-size: 15px; font-weight: 600; line-height: 1.3; color: var(--ink-soft);
  }
  .contacts {
    position: absolute; left: 295px; top: 166px;
    list-style: none;
    font-size: 15px; font-weight: 600; line-height: 1.35; color: var(--ink-soft);
  }
  .contacts li { display: flex; align-items: center; gap: 8px; }
  .contacts svg, .address svg { flex: none; }
  .web-highlight { color: var(--orange); }
  .swoosh { position: absolute; left: 0; bottom: 0; width: 580px; height: 110px; display: block; }
</style>
</head>
<body>

<section class="card card-front" aria-label="Business card front">
  <div class="front-lockup">
    <span class="front-mark"></span>
    <p class="front-name">Bright Harbor<br>Educational Consulting</p>
  </div>
  <p class="front-web">www.brightharboredu.com</p>
</section>

<section class="card card-back" aria-label="Business card back">
  <div class="back-lockup">
    <span class="back-mark"></span>
    <p class="back-name">Bright Harbor<br>Educational Consulting</p>
  </div>

  <div class="person">
    <p class="person-name">Daniel Marsh</p>
    <p class="person-role">director</p>
  </div>

  <div class="address">
    <svg width="16" height="16" viewBox="0 0 16 16" aria-hidden="true">
      <path d="M8 1 L15 8 H13 V15 H3 V8 H1 Z" fill="var(--orange)"/>
    </svg>
    <p>P.O Box 482<br>Cedar Lake Falls<br>Illinois 60119-0482</p>
  </div>

  <ul class="contacts">
    <li>
      <svg width="14" height="14" viewBox="0 0 14 14" aria-hidden="true">
        <path d="M3 1 C1 2 1 5 4 9 C7 13 10 13 12 11 L10 8 L8 9 C7 8 6 7 5 5 L6 4 Z" fill="var(--orange)"/>
      </svg><span>555 214 7730</span></li>
    <li>
      <svg width="14" height="14" viewBox="0 0 14 14" aria-hidden="true">
        <rect x="1" y="5" width="12" height="7" rx="1" fill="var(--orange)"/>
        <rect x="3" y="1" width="8" height="5" fill="var(--orange)" opacity="0.7"/>
      </svg><span>555 000 0000</span></li>
    <li>
      <svg width="14" height="14" viewBox="0 0 14 14" aria-hidden="true">
        <rect x="1" y="3" width="12" height="9" rx="1" fill="var(--orange)"/>
        <path d="M1 3 L7 8 L13 3" stroke="#fff" stroke-width="1.2" fill="none"/>
      </svg><span>brightharboredu.com</span></li>
    <li>
      <svg width="14" height="14" viewBox="0 0 14 14" aria-hidden="true">
        <circle cx="7" cy="7" r="6" fill="var(--orange)"/>
      </svg><span>www.<span class="web-highlight">brightharboredu</span>.com</span></li>
  </ul>

  <svg class="swoosh" viewBox="0 0 580 110" preserveAspectRatio="none" aria-hidden="true">
    <path d="M0 18 C200 40 400 60 580 66 L580 110 L0 110 Z" fill="var(--orange)"/>
    <path d="M0 50 C200 58 400 72 580 80 L580 110 L0 110 Z" fill="var(--blue-mid)"/>
    <path d="M0 70 C220 74 420 84 580 88 L580 110 L0 110 Z" fill="var(--blue-deep)"/>
  </svg>
</section>

</body>
</html>
```